Southwest Marketing Postcard for Donor Egg Agency

We are an egg donor agency which is a leader in the field in the Southwest United States. We offer a unique program that provides pre-screeend egg donors to infertile women. We are planning this marketing campaign to Infertility clinics and their donor coordinators. We actually want two versions so that we can mail them out 3-4 weeks apart. We would like the design to convery our professiohalsim (Im an RN with 18+ years infertility experience) and our unique mix of ethnicities, education and talents of our egg donors. We also "pre-screen" all potential donors with AMh blood testing and background checks and personally interview every candidate
Updates

Project Deadline Extended Reason: I was called out of town for an emergency and then was traveling overseas and didn't take my computer. I thought I could decide when I returned. I would like to see these submissions again.6365708636570763657006365695639064963656966394705Thank you very much,Joan Added Monday, June 29, 2015

Target Market(s)

Infertility Physicians and their stafrf

Industry/Entity Type

Marketing

Font styles to use
Serif

Requirements
Must have
• Moms and Dads who are a "bit" older and their child (infants to toddlers)
• Photos of young women (who would represent the egg donors)
• Correct info about our company
Nice to have
• I want to make the person reading the postcard want to go tell their patients about us....I want to feel fresh and exciting....different and new

```html
<!DOCTYPE html>
<html lang="en">
<head>
<meta charset="utf-8">
<title>Cradle Bridge Postcards</title>
<link rel="stylesheet" href="https://fonts.googleapis.com/css2?family=Open+Sans:wght@400;600;700&family=Roboto+Condensed:ital,wght@1,400&display=swap">
<style>
  :root{
    --sky:#d8eef9;
    --sky-deep:#c6e5f5;
    --orange:#ec8a1f;
    --blue:#1d4f9e;
    --band:#1b5fae;
    --pill:#1a7cc0;
    --panel:#ececec;
    --text:#555;
    --ink:#111;
    --page:#e9e6e1;
  }
  *{box-sizing:border-box;margin:0;padding:0}
  html,body{width:1031px;height:1200px;overflow:hidden;background:var(--page);font-family:"Open Sans",Arial,sans-serif}
  .postcard{position:absolute;width:862px;height:560px;background:#fff;overflow:hidden;box-shadow:0 6px 16px rgba(0,0,0,.25)}
  .postcard--front{left:58px;top:22px}
  .postcard--back{left:118px;top:618px}
  .header{position:absolute;left:0;top:0;width:862px;height:150px}
  .brand{position:absolute;left:26px;top:40px}
  .brand__row{display:flex;align-items:center;gap:10px}
  .brand__name{font-weight:700;font-size:37px;color:var(--blue);letter-spacing:-1px;line-height:1}
  .brand__mark{width:26px;height:26px;background:var(--orange)}
  .brand__tagline{font-size:12.5px;color:var(--orange);letter-spacing:.6px;margin-top:2px}
  .slogan{position:absolute;right:38px;top:52px;font-family:"Roboto Condensed",Arial,sans-serif;font-style:italic;font-size:29px;color:var(--orange)}
  .photo{position:absolute}
  .panel{position:absolute;background:var(--panel)}
  .band{position:absolute;left:0;bottom:0;width:100%;height:30px;background:var(--band)}
  .benefits{list-style:none;position:absolute;left:14px;top:50px;width:300px}
  .benefits li{position:relative;padding-left:24px;font-size:16px;line-height:24px;color:var(--text);margin-bottom:8px}
  .benefits svg{position:absolute;left:0;top:3px}
  .cta{position:absolute;text-align:left}
  .cta__note{color:var(--ink);line-height:1.3}
  .cta__line{color:var(--blue);display:flex;align-items:center;gap:4px}
  .cta__phone{font-weight:700}
  .front .cta{left:56px;top:313px}
  .front .cta__note{font-size:15px;margin-bottom:6px}
  .front .cta__line{font-size:18px;margin-left:-20px}
  .difference{position:absolute;left:16px;top:26px;width:238px}
  .difference h2{font-weight:400;font-size:16.5px;line-height:25px;color:var(--blue)}
  .difference p{margin-top:13px;font-size:13px;line-height:18px;color:var(--text);text-align:justify}
  .back .cta{left:16px;top:231px}
  .back .cta__note{font-size:12px;margin-left:35px;margin-bottom:4px}
  .back .cta__line{font-size:15px}
  .url{position:absolute;left:63px;top:437px;width:380px;height:45px;background:var(--pill);border-radius:0 0 22px 22px;color:#fff;font-size:24px;letter-spacing:.8px;padding:5px 0 0 15px}
  .stamp{position:absolute;left:757px;top:143px;width:69px;height:55px;border:1px solid #777}
  .address-line{position:absolute;left:613px;width:210px;height:1px;background:#777}
</style>
</head>
<body>

<section class="postcard postcard--front front">
  <svg class="header" viewBox="0 0 862 150" aria-hidden="true">
    <defs><linearGradient id="skyA" x1="0" y1="0" x2="1" y2="0"><stop offset="0" stop-color="#d3ecf8"/><stop offset="1" stop-color="#dff1fa"/></linearGradient></defs>
    <path d="M0 0H862V120Q620 150 420 140Q200 128 0 120Z" fill="url(#skyA)"/>
  </svg>
  <div class="brand">
    <div class="brand__row"><span class="brand__name">Cradle Bridge</span><span class="brand__mark"></span></div>
    <div class="brand__tagline">the bridge to extraordinary egg donors</div>
  </div>
  <div class="slogan">Help a family with the gift of a child!</div>
  <div class="photo" role="img" aria-label="Photo of a mother and father lying on a white rug with their newborn twins" style="left:0;top:138px;width:522px;height:392px;background:radial-gradient(ellipse at 55% 55%,#f4efea 0%,#e8ddd3 55%,#f5f3f1 100%)"></div>
  <div class="panel" style="left:522px;top:128px;width:326px;height:402px">
    <ul class="benefits">
      <li><svg width="18" height="18" viewBox="0 0 18 18"><circle cx="9" cy="9" r="9" fill="var(--orange)"/><path d="M7 5l4 4-4 4" stroke="#fff" stroke-width="2" fill="none"/></svg>We have 18+ years infertility experience</li>
      <li><svg width="18" height="18" viewBox="0 0 18 18"><circle cx="9" cy="9" r="9" fill="var(--orange)"/><path d="M7 5l4 4-4 4" stroke="#fff" stroke-width="2" fill="none"/></svg>We offer a unique program that provides pre-screened egg donors to infertile women.</li>
      <li><svg width="18" height="18" viewBox="0 0 18 18"><circle cx="9" cy="9" r="9" fill="var(--orange)"/><path d="M7 5l4 4-4 4" stroke="#fff" stroke-width="2" fill="none"/></svg>We also "pre-screen" all potential donors with AMH blood testing and background checks and personally interview every candidate.</li>
    </ul>
    <div class="cta">
      <p class="cta__note">Contact us today for a free,<br>no obligation consultation:</p>
      <p class="cta__line">Contact Us
        <svg width="20" height="20" viewBox="0 0 20 20"><circle cx="10" cy="10" r="8.5" fill="none" stroke="var(--blue)" stroke-width="1.6"/><path d="M7 5.5l1.6 2.2-1 1.2q1 2 3 3l1.2-1 2.2 1.6-1 1.6q-4-.5-6.6-4.8Q6 6.6 7 5.5z" fill="var(--blue)"/></svg>
        <span class="cta__phone">(555) 214-0388</span></p>
    </div>
  </div>
  <div class="band"></div>
</section>

<section class="postcard postcard--back back">
  <svg class="header" viewBox="0 0 862 150" aria-hidden="true">
    <defs><linearGradient id="skyB" x1="0" y1="0" x2="1" y2="0"><stop offset="0" stop-color="#d3ecf8"/><stop offset="1" stop-color="#dff1fa"/></linearGradient></defs>
    <path d="M0 0H862V120Q620 145 420 136Q200 125 0 112Z" fill="url(#skyB)"/>
  </svg>
  <div class="brand">
    <div class="brand__row"><span class="brand__name">Cradle Bridge</span><span class="brand__mark"></span></div>
    <div class="brand__tagline">the bridge to extraordinary egg donors</div>
  </div>
  <div class="slogan">Help a family with the gift of a child!</div>
  <div class="photo" role="img" aria-label="Photo of a smiling young woman sitting with friends outdoors" style="left:0;top:122px;width:233px;height:315px;background:linear-gradient(160deg,#c9c2b6 0%,#9c7e66 45%,#6f7a70 100%)"></div>
  <div class="panel" style="left:233px;top:138px;width:266px;height:299px;border-radius:0 0 10px 0">
    <div class="difference">
      <h2>The Cradle Bridge Difference<br>What makes us different?</h2>
      <p>Cradle Bridge is dedicated to our client's well-being. Our team works hard to provide the best possible experience. We know struggling with fertility can be difficult. We are here to help make the process easier.</p>
    </div>
    <div class="cta">
      <p class="cta__note">Contact us today for a free,<br>no obligation consultation:</p>
      <p class="cta__line">Contact Us
        <svg width="17" height="17" viewBox="0 0 20 20"><circle cx="10" cy="10" r="8.5" fill="none" stroke="var(--blue)" stroke-width="1.6"/><path d="M7 5.5l1.6 2.2-1 1.2q1 2 3 3l1.2-1 2.2 1.6-1 1.6q-4-.5-6.6-4.8Q6 6.6 7 5.5z" fill="var(--blue)"/></svg>
        <span class="cta__phone">(555) 214-0388</span></p>
    </div>
  </div>
  <div class="url">www.cradlebridgedonors.com</div>
  <div class="stamp"></div>
  <div class="address-line" style="top:261px"></div>
  <div class="address-line" style="top:300px"></div>
  <div class="address-line" style="top:339px"></div>
  <div class="band"></div>
</section>

</body>
</html>
```